Gemstone Jewelry Online Shop Needs a Banner Design

We need a banner design for a new gemstone Jewelry Online Shop based in the U.S. called "Velanor". One of our selling points is "never fall out of stone". We want to express: a Party Queen doesn't need to worry whenever she may meet an embarrassing moment - a stone of jewelry falls out at a very important occasion. Please insert one of attached images. Please visit our website for more details: http://velanor-shop.example/
The banner size: 1200*628
If you think other images at our website are better, please let us know. Many thanks and looking forward to your beautiful and creative designs!

Industry/Entity Type

Jewelry

```html
<!DOCTYPE html>
<html lang="en">
<head>
<meta charset="utf-8">
<title>Velanor — Never Fall Out of Stone</title>
<link rel="stylesheet" href="https://fonts.googleapis.com/css2?family=Questrial&display=swap">
<style>
  :root {
    --bg-light: #f7f7f8;
    --bg-mid: #e4e5e8;
    --bg-shade: #cfd1d5;
    --ink: #3a3a3c;
    --ruby: #c8121a;
    --ruby-deep: #8e070d;
    --ruby-light: #ef3a3f;
    --silver: #d9dbdf;
    --silver-deep: #b9bcc2;
    --white: #ffffff;
  }
  * { margin: 0; padding: 0; box-sizing: border-box; }
  html, body { width: 1200px; height: 628px; overflow: hidden; }
  body { font-family: "Questrial", "Century Gothic", sans-serif; }

  .banner {
    position: relative;
    width: 1200px;
    height: 628px;
    overflow: hidden;
    background: radial-gradient(ellipse at 72% 40%, var(--white) 0%, var(--bg-light) 35%, var(--bg-mid) 100%);
  }

  .facets { position: absolute; inset: 0; width: 1200px; height: 628px; }

  .headline {
    position: absolute;
    left: 114px;
    top: 186px;
    font-size: 56px;
    line-height: 68px;
    font-weight: 400;
    letter-spacing: 1.5px;
    word-spacing: -4px;
    color: var(--ink);
    text-transform: uppercase;
    white-space: nowrap;
  }

  .cta {
    position: absolute;
    left: 115px;
    top: 365px;
    width: 224px;
    height: 68px;
    border-radius: 3px;
    background: linear-gradient(180deg, var(--ruby-light) 0%, var(--ruby) 45%, var(--ruby-deep) 100%);
    box-shadow: 0 1px 2px rgba(0,0,0,0.25);
    display: flex;
    align-items: center;
    justify-content: center;
    color: var(--white);
    font-size: 27px;
    text-decoration: none;
    white-space: nowrap;
  }

  .cta-reflection {
    position: absolute;
    left: 115px;
    top: 435px;
    width: 224px;
    height: 68px;
    border-radius: 3px;
    background: linear-gradient(180deg, var(--ruby-deep) 0%, var(--ruby) 100%);
    color: var(--white);
    font-size: 27px;
    display: flex;
    align-items: center;
    justify-content: center;
    white-space: nowrap;
    transform: scaleY(-1);
    opacity: 0.35;
    -webkit-mask-image: linear-gradient(0deg, rgba(0,0,0,0.9) 0%, rgba(0,0,0,0) 55%);
    mask-image: linear-gradient(0deg, rgba(0,0,0,0.9) 0%, rgba(0,0,0,0) 55%);
  }

  .product-photo {
    position: absolute;
    left: 660px;
    top: 100px;
    width: 355px;
    height: 380px;
    border-radius: 50%;
    background: radial-gradient(circle at 50% 45%, var(--ruby) 0%, var(--ruby-deep) 32%, var(--silver-deep) 33%, var(--silver) 70%, var(--bg-light) 100%);
    box-shadow: 0 6px 18px rgba(0,0,0,0.12);
  }

  .product-reflection {
    position: absolute;
    left: 700px;
    top: 488px;
    width: 275px;
    height: 140px;
    border-radius: 50% 50% 0 0 / 40% 40% 0 0;
    background: linear-gradient(180deg, rgba(185,188,194,0.45) 0%, rgba(228,229,232,0) 90%);
  }
</style>
</head>
<body>
  <main class="banner">
    <svg class="facets" viewBox="0 0 1200 628" aria-hidden="true">
      <polygon points="0,0 260,0 120,280 0,360" fill="var(--bg-mid)" opacity="0.55"/>
      <polygon points="260,0 560,0 300,628 160,628" fill="var(--bg-shade)" opacity="0.35"/>
      <polygon points="330,80 470,180 300,628 230,628" fill="var(--white)" opacity="0.45"/>
      <polygon points="0,360 120,280 160,628 0,628" fill="var(--bg-shade)" opacity="0.4"/>
      <polygon points="560,0 720,0 420,628 300,628" fill="var(--white)" opacity="0.35"/>
      <polygon points="1000,0 1200,0 1200,200" fill="var(--bg-mid)" opacity="0.5"/>
      <polygon points="1060,628 1200,420 1200,628" fill="var(--bg-shade)" opacity="0.35"/>
    </svg>

    <h1 class="headline">Never Fall<br>Out of Stone</h1>

    <a class="cta" href="http://velanor-shop.example/">SHOP NOW</a>
    <div class="cta-reflection" aria-hidden="true">SHOP NOW</div>

    <div class="product-photo" role="img" aria-label="Sterling silver flower cocktail ring with an oval red garnet centre in a halo of small clear stones, surrounded by eight pear-shaped garnet petals"></div>
    <div class="product-reflection" role="img" aria-label="Soft reflection of the ring on a glossy surface"></div>
  </main>
</body>
</html>
```